Dermatology Flyers - 3 x A4 folded to DL flyers

I need 3 different flyers for my 3 brands for patients to know what we do. The three flyers are for the following three brands:
1. Marlowe Skin Clinics Australia
2. Brevant Skin Clinics Australia
3. Tolvera Skin Clinics Australia

I'd like to include information about (1) who we are (dermatologist led, dr keldric Outhwaite) (2) what we do (our mission, our treatments) (3) process to see us (see about us page on website)

websites are:
marloweskinclinics.com.au
tolveraskinclinics.com.au
brevantskinclinicsaustralia.com.au

and logos are attached

we plan to be australia wide group of clinics, so I don't want any location information on the flyer, just the website addresses

if we can incorporate: "learn more about our sister companies" with the logos and websites of the other two brands on the back page of each flyer that would be great

please contact me if you'd like any further information

Industry/Entity Type

Medical, Dermatology

Requirements
Must have
• 3 flyers, size a4 folded to DL

```html
<!DOCTYPE html>
<html lang="en">
<head>
<meta charset="utf-8">
<title>Brevant Skin Clinics Australia – DL Flyer</title>
<link href="https://fonts.googleapis.com/css2?family=Source+Sans+3:wght@400;600;700&display=swap" rel="stylesheet">
<style>
:root{
  --page:#e8e8e8;
  --label:#66727c;
  --green:#22b04b;
  --grey:#a6abb8;
  --slate:#67737d;
  --ink:#2a2a2a;
  --heading:#2b2f36;
  --deep:#1d3b24;
  --white:#ffffff;
}
*{margin:0;padding:0;box-sizing:border-box}
html,body{width:848px;height:1200px;overflow:hidden}
body{background:var(--page);position:relative;font-family:"Source Sans 3",sans-serif;color:var(--ink)}
.side-label{position:absolute;font-size:25px;color:var(--label);letter-spacing:.5px;font-weight:400}
.side-label.inside{left:35px;top:48px}
.side-label.outside{right:15px;top:610px}
.sheet{position:absolute;left:126px;width:611px;height:475px;background:var(--white);overflow:hidden}
.sheet.inner{top:96px}
.sheet.outer{top:646px}
.abs{position:absolute}
.panel-bg{position:absolute;top:0;height:100%}
h2{font-size:12.5px;font-weight:700;color:var(--heading);line-height:1.1;margin-bottom:1px}
.body{font-size:7.1px;line-height:9.5px;text-align:justify}
.body p+p{margin-top:9.5px}
.on-dark{color:var(--white)}
.on-dark h2{color:var(--white)}
.photo{position:absolute}
.swoosh{position:absolute;left:0;top:0}
.contact{font-size:12px;color:var(--white);display:flex;align-items:center;gap:4px;white-space:nowrap}
.contact.web{font-weight:700;font-size:10px}
.brand-name{color:var(--white);font-weight:600;font-size:13px;letter-spacing:2.2px;text-align:center;line-height:16px;text-transform:uppercase}
.dot{width:12px;height:12px;border-radius:50%;background:var(--white);flex:none}
.centered{text-align:center}
.lead{font-size:10.2px;line-height:12.6px;color:var(--white)}
.bold-head{font-size:13px;font-weight:700;line-height:13.6px;color:var(--white)}
.cta-button{background:var(--heading);color:var(--white);font-weight:700;font-size:12.5px;line-height:13px;border-radius:7px;text-align:center;padding:4px 0}
.foot{font-size:10px;line-height:12.6px;color:var(--ink)}
</style>
</head>
<body>

<div class="side-label inside">INSIDE</div>

<section class="sheet inner">
  <div class="panel-bg" style="left:204px;width:203px;background:var(--grey)"></div>
  <div class="panel-bg" style="left:407px;width:204px;background:var(--slate)"></div>

  <div class="photo" role="img" aria-label="Photo of hands squeezing moisturising cream from a tube" style="left:204px;top:302px;width:203px;height:90px;background:linear-gradient(135deg,#d9c2b0,#efe6df 55%,#c9cdd2)"></div>
  <div class="photo" role="img" aria-label="Photo looking up into the lamps of a UVB phototherapy unit" style="left:407px;top:103px;width:204px;height:109px;background:radial-gradient(ellipse at 50% 100%,#2d4e7e 0%,#6f9bd0 30%,#dbe8f6 75%)"></div>

  <div class="abs" style="left:25px;top:24px;width:161px">
    <h2>About Eczema</h2>
    <div class="body">
      <p>Eczema, or dermatitis, is a common condition that results in a barrier dysfunction of the skin. In various forms, it affects up to 25% of children and 10% of adults. Patients with eczema present with itchy rashes, which may involve any area of the body. There may be a genetic component to this condition, with patients often having other family members with eczema.</p>
      <p>Some with eczema may have an allergic tendency, especially if they have ‘Atopic Dermatitis’. There may also be an increased association with ‘allergic’ conditions such as asthma, hayfever, allergic conjunctivitis.</p>
      <p>Eczema often starts in infancy or early childhood, and even though many patients may spontaneously improve as they grow into adolescence, some will continue having flares in adulthood.</p>
      <p>The skin barrier of eczema patients is compromised, meaning that where normal skin will keep moisture in and bacteria out, the skin of eczema patients has microscopic ‘cracks’ that let moisture out and allow bacteria in.</p>
    </div>
  </div>
  <div class="abs" role="img" aria-label="Diagram comparing the skin layers of intact skin and eczema skin, with moisture and bacteria arrows" style="left:8px;top:293px;width:190px;height:92px;background:linear-gradient(90deg,#f6d8c8,#fbe9df 50%,#f6d8c8)"></div>
  <div class="abs" style="left:54px;top:387px;font-size:6px">Intact Skin</div>
  <div class="abs" style="left:136px;top:387px;font-size:6px">Eczema</div>

  <div class="abs" style="left:225px;top:24px;width:161px">
    <h2>Our Eczema Treatments</h2>
    <div class="body" style="text-align:left">
      <p>The best components for eczema patients to support their skin is to :<br>1. Use moisturiser to keep moisture in ALL. THE. TIME.<br>2. Use a good home care program to keep your skin intact and not aggravate or induce flares.<br>3. Use topical therapy &amp; UVB phototherapy to address the flares as required,<br>4. Use antihistamines to reduce the itch if you can’t sleep,<br>5. Use antibiotics to address any infections that have been able to penetrate your skin, and<br>6. Use biologics for severe eczema if required</p>
    </div>
    <h2 style="margin-top:14px">Home Care Programme</h2>
    <div class="body">
      <p>Your daily actions will have a significant effect on the success of your eczema treatment, so it’s really important to get it right!</p>
      <p>Our home care program for you will include understanding your trigger factors, how your family can support you at home, how to apply your home care over the counter and prescription topicals successfully, the low down on wet wraps and ensuring your bathroom routine is keeping your skin intact as much as possible.</p>
    </div>
  </div>

  <div class="abs on-dark" style="left:423px;top:24px;width:161px">
    <h2>Topical Therapy</h2>
    <div class="body"><p>Over the counter and prescription topical medication are the first line of defence on early stage eczema, and is always used as an adjunct to other treatment options if your eczema has progressed. They will help sooth your skin and reduce your flares.</p></div>
  </div>
  <div class="abs on-dark" style="left:423px;top:217px;width:161px">
    <h2>UVB Phototherapy</h2>
    <div class="body" style="margin-top:3px"><p>UVB phototherapy is a clinically proven, safe treatment that provides many of our patients with relief from the symptoms of eczema. In Australia, these treatments are usually bulk billed.</p></div>
    <h2 style="margin-top:6px">Systemic Therapy</h2>
    <div class="body" style="margin-top:3px;text-align:left"><p>Your dermatologist will be able to discuss new biologic therapies available to chronic eczema patients who have not been able to obtain relief through other methods.</p></div>
  </div>

  <svg class="swoosh" width="611" height="475" viewBox="0 0 611 475" aria-hidden="true">
    <path d="M0,401 C250,392 470,370 560,325 Q600,305 611,290 L611,475 L0,475 Z" fill="var(--green)"/>
  </svg>

  <div class="abs centered" style="left:430px;top:371px;width:160px;color:var(--white);font-size:11.5px;line-height:12.5px">Book Your Free<br>Initial Consultation.</div>
  <div class="abs brand-name" style="left:425px;top:402px;width:170px">Brevant Skin<br>Clinics Australia</div>

  <div class="abs" style="left:48px;top:409px;display:grid;gap:3px">
    <div class="contact"><span class="dot"></span>BrevantClinics</div>
    <div class="contact"><span class="dot"></span>@brevantclinics</div>
  </div>
  <div class="abs" style="left:212px;top:420px;display:flex;justify-content:center;width:196px">
    <div class="contact web">
      <svg width="11" height="11" viewBox="0 0 12 12" aria-hidden="true"><g fill="none" stroke="var(--white)" stroke-width="1"><circle cx="6" cy="6" r="5.3"/><ellipse cx="6" cy="6" rx="2.4" ry="5.3"/><path d="M.7 6h10.6M1.6 3.3h8.8M1.6 8.7h8.8"/></g></svg>
      brevantskinclinicsaustralia.com.au</div>
  </div>
</section>

<div class="side-label outside">OUTSIDE</div>

<section class="sheet outer">
  <svg class="swoosh" width="611" height="475" viewBox="0 0 611 475" aria-hidden="true">
    <path d="M0,0 L611,0 L611,290 Q590,330 520,355 C400,385 200,395 0,400 Z" fill="var(--green)"/>
  </svg>

  <div class="photo" role="img" aria-label="Photo of a doctor in scrubs reassuring an older patient" style="left:204px;top:125px;width:203px;height:108px;background:linear-gradient(120deg,#8a94a0,#c9b8a4 45%,#6f9cc8)"></div>
  <div class="photo" role="img" aria-label="Photo of a baby's leg with an eczema rash" style="left:407px;top:125px;width:204px;height:108px;background:linear-gradient(110deg,#a79f94,#e9cbbb 50%,#d8c6b6)"></div>
  <div class="photo" role="img" aria-label="Portrait of the specialist dermatologist" style="left:45px;top:124px;width:113px;height:113px;border-radius:50%;background:radial-gradient(circle at 50% 40%,#f1f1f1,#cfd2d6 70%,#9aa1a8)"></div>

  <div class="abs centered bold-head" style="left:32px;top:34px;width:140px">Have a specialist review today &amp; start your bulk billed treatments tomorrow!</div>
  <div class="abs centered lead" style="left:224px;top:34px;width:162px">Access support &amp; treatments close to home, no matter where you live. Providing access to specialist plans and treatments outside of capital cities.</div>
  <div class="abs brand-name" style="left:425px;top:40px;width:170px;font-size:14px;line-height:18px">Brevant Skin<br>Clinics Australia</div>

  <div class="abs centered lead" style="left:22px;top:246px;width:160px">“With more than a decade of experience with eczema, treating thousands of patients successfully throughout Australia, helping eczema patients along their journey is a pleasure and a passion for me”</div>
  <div class="abs centered" style="left:18px;top:334px;width:168px;color:var(--white);font-weight:700;font-size:10px;line-height:12.6px">Dr Keldric Outhwaite<br>MBBS FACD<br>Specialist Dermatologist</div>

  <div class="abs centered lead" style="left:224px;top:246px;width:162px">Eczema affects around 6 million children and 2.5 million adults in Australia and can be well managed with a comprehensive treatment plan of home care, prescriptions and phototherapy in most cases.</div>

  <div class="abs centered" style="left:424px;top:246px;width:170px;font-weight:700;font-size:13px;line-height:13.6px;color:var(--deep)">Our eczema treatments include important home care program information, topical creams, UVB phototherapy and prescription medication.</div>

  <div class="abs cta-button" style="left:443px;top:365px;width:123px">Book Your Free<br>Initial Consultation</div>

  <div class="abs centered foot" style="left:20px;top:404px;width:164px">
    <div style="font-weight:700;font-size:11.5px;color:var(--heading)">Our other websites are:</div>
    <div>marloweskinclinics.com.au</div>
    <div>tolveraskinclinics.com.au</div>
  </div>
  <div class="abs" style="left:212px;top:421px;display:flex;justify-content:center;width:196px">
    <div class="contact web" style="color:var(--heading)">
      <svg width="11" height="11" viewBox="0 0 12 12" aria-hidden="true"><g fill="none" stroke="var(--heading)" stroke-width="1"><circle cx="6" cy="6" r="5.3"/><ellipse cx="6" cy="6" rx="2.4" ry="5.3"/><path d="M.7 6h10.6M1.6 3.3h8.8M1.6 8.7h8.8"/></g></svg>
      brevantskinclinicsaustralia.com.au</div>
  </div>
  <div class="abs centered foot" style="left:422px;top:412px;width:166px">Find out which treatment plan will work for you.&nbsp; Get in touch</div>
</section>

</body>
</html>
```